Pine Arbor Table & Chair Rentals

We need a business card for a table and chair rental company. We rent tables and chairs for weddings, funerals, business events and parties. We want something that looks clean and elegant while not being too busy. We would like colors in the green and blue hues and avoiding anything orange. We want to make sure the font is large enough to be seen easily.

Target Market(s)

Wedding & Event Rentals

Industry/Entity Type

Events

Contact Information for Business Card

Pine Arbor, sales@pinearborrentals.example, pinearborrentals.example, 555-218-0937

Requirements
Must have
• Easy to read font
Should not have
• Orange anywhere in the design

```html
<!DOCTYPE html>
<html lang="en">
<head>
<meta charset="utf-8">
<title>Pine Arbor Table &amp; Chair Rentals – Business Card</title>
<link rel="stylesheet" href="https://fonts.googleapis.com/css2?family=Anton&family=Cormorant+Garamond:ital,wght@1,500&family=Arimo&display=swap">
<style>
  :root {
    --card-green: #52c97a;
    --card-border: #8a8a8a;
    --brand-blue: #0000ff;
    --tagline-grey: #333333;
    --services-purple: #4b3d8f;
    --photo-light: #cfeee0;
    --photo-blue: #7fb6d6;
    --photo-deep: #3f8a6a;
  }
  html, body {
    margin: 0;
    padding: 0;
    width: 1200px;
    height: 728px;
    overflow: hidden;
    background: #ffffff;
  }
  .business-card {
    display: block;
    width: 1200px;
    height: 728px;
  }
  .brand-name {
    font-family: "Anton", "Oswald", sans-serif;
    fill: var(--brand-blue);
  }
  .tagline {
    font-family: "Cormorant Garamond", "Times New Roman", serif;
    font-style: italic;
    font-weight: 500;
    fill: var(--tagline-grey);
  }
  .services-line,
  .contact-line {
    font-family: "Arimo", Arial, sans-serif;
    fill: var(--services-purple);
  }
</style>
</head>
<body>
<svg class="business-card" viewBox="0 0 1200 728" xmlns="http://www.w3.org/2000/svg">
  <defs>
    <linearGradient id="event-photo-tone" x1="0" y1="0" x2="1" y2="0">
      <stop offset="0" stop-color="var(--photo-light)"/>
      <stop offset="0.35" stop-color="var(--photo-blue)"/>
      <stop offset="0.65" stop-color="var(--photo-deep)" stop-opacity="0.6"/>
      <stop offset="1" stop-color="var(--card-green)" stop-opacity="0"/>
    </linearGradient>
  </defs>

  <rect class="card-background" x="0.5" y="0.5" width="1199" height="727"
        fill="var(--card-green)" stroke="var(--card-border)" stroke-width="1"/>

  <polygon class="event-photo" role="img"
           aria-label="Photo of a tented banquet hall set with white-draped tables and chairs with blue sashes"
           points="76,188 746,27 846,439 176,600"
           fill="url(#event-photo-tone)"/>

  <text class="brand-name" x="145" y="214" font-size="186"
        textLength="927" lengthAdjust="spacingAndGlyphs">PINE ARBOR</text>

  <text class="tagline" x="796" y="277" font-size="58"
        textLength="374" lengthAdjust="spacingAndGlyphs">Chairs &amp; Tables</text>
  <text class="tagline" x="865" y="331" font-size="46"
        textLength="224" lengthAdjust="spacingAndGlyphs">Rental  for</text>
  <text class="tagline" x="811" y="385" font-size="58"
        textLength="297" lengthAdjust="spacingAndGlyphs">All events</text>

  <g class="contact-details" text-anchor="end">
    <text class="contact-line" x="1140" y="505" font-size="26">555-218-0937</text>
    <text class="contact-line" x="1140" y="548" font-size="26">sales@pinearborrentals.example</text>
    <text class="contact-line" x="1140" y="591" font-size="26">pinearborrentals.example</text>
  </g>

  <text class="services-line" x="87" y="701" font-size="26"
        textLength="1039" lengthAdjust="spacingAndGlyphs">We Rent Tables &amp; Chairs for Weddings, Funerals, Business Events and Parties</text>
</svg>
</body>
</html>
```